Business card design needed

am looking for a fun and funky design to match our moto, seriously fun swimwear and fashion for girls.

We manufacture and retail girls swimwear and fashion in Australia. Our designs are fun loving and funky. I would like to use bright fuschia to match our website www.breezyplum.com.au. We target a higher end market so need it to reflect this.

Industry/Entity Type

Fashion

Contact Information for Business Card

Breezy Plum logo,
Maddie Lorne
(07) 35517204
admin@breezyplum.com.au
www.breezyplum.com.au

Logo Text

Breezy Plum

```html
<!DOCTYPE html>
<html lang="en">
<head>
<meta charset="utf-8">
<title>Breezy Plum — Business Cards</title>
<link rel="stylesheet" href="https://fonts.googleapis.com/css2?family=Open+Sans:wght@400;700&display=swap">
<style>
  :root {
    --fuchsia: #b8146e;
    --fuchsia-deep: #9a0c58;
    --fuchsia-bright: #cc2282;
    --blush: #fbe3ef;
    --blush-light: #ffffff;
    --petal: #f2a9cf;
    --backdrop: #2b2b2b;
    --white: #ffffff;
  }
  * { box-sizing: border-box; margin: 0; padding: 0; }
  html, body { width: 1200px; height: 900px; overflow: hidden; }
  body {
    background: var(--backdrop);
    font-family: "Open Sans", Arial, sans-serif;
    position: relative;
  }
  .card {
    position: absolute;
    width: 540px;
    height: 320px;
    border-radius: 4px;
    overflow: hidden;
    box-shadow: 0 14px 32px rgba(0,0,0,0.55);
  }

  /* Front card */
  .card--front {
    left: 70px;
    top: 120px;
    background: linear-gradient(180deg, var(--blush-light) 0%, var(--blush) 100%);
  }
  .brand {
    position: absolute;
    display: flex;
    align-items: center;
    gap: 12px;
    color: var(--fuchsia);
    font-weight: 400;
  }
  .card--front .brand {
    left: 150px;
    top: 72px;
    font-size: 40px;
  }
  .brand__dot {
    width: 34px;
    height: 34px;
    border-radius: 50%;
    background: var(--fuchsia-bright);
  }
  .front__band {
    position: absolute;
    left: 0; right: 0; bottom: 0;
    height: 70px;
    background: var(--fuchsia);
  }
  .front__band-line {
    position: absolute;
    left: 0; right: 0; bottom: 70px;
    height: 4px;
    background: var(--petal);
  }
  .tab {
    position: absolute;
    background: var(--fuchsia);
    border-radius: 12px 12px 0 0;
    color: var(--white);
  }
  .tab--name {
    left: 0;
    bottom: 70px;
    width: 258px;
    height: 78px;
    border-radius: 0 14px 0 0;
    display: flex;
    align-items: flex-end;
    padding: 0 0 14px 36px;
    font-weight: 700;
    font-size: 24px;
  }
  .tab--contact {
    right: 0;
    top: 150px;
    width: 262px;
    height: 74px;
    border-radius: 14px 0 0 14px;
    padding: 10px 0 0 24px;
    font-size: 12.5px;
    line-height: 1.35;
  }

  /* Back card */
  .card--back {
    left: 590px;
    top: 470px;
    background: radial-gradient(ellipse at 75% 30%, var(--fuchsia-deep) 0%, var(--fuchsia) 55%, var(--fuchsia-bright) 100%);
  }
  .card--back .brand {
    right: 48px;
    top: 52px;
    color: var(--petal);
    font-size: 46px;
  }
  .back__ornament {
    position: absolute;
    left: 0;
    bottom: 0;
    width: 330px;
    height: 170px;
    background: linear-gradient(90deg, rgba(242,169,207,0.55) 0%, rgba(242,169,207,0.25) 70%, rgba(242,169,207,0) 100%);
    border-radius: 0 90px 0 0;
  }
</style>
</head>
<body>
  <section class="card card--front">
    <div class="brand"><span class="brand__dot"></span><span class="brand__name">Breezy Plum</span></div>
    <div class="tab tab--contact">
      <p>(07) 35517204</p>
      <p>admin@breezyplum.com.au</p>
      <p>www.breezyplum.com.au</p>
    </div>
    <div class="front__band-line"></div>
    <div class="tab tab--name">Maddie Lorne</div>
    <div class="front__band"></div>
  </section>

  <section class="card card--back">
    <div class="brand"><span class="brand__name">Breezy Plum</span></div>
    <div class="back__ornament" role="img" aria-label="Decorative pale pink flourish of curling swirls"></div>
  </section>
</body>
</html>
```